Card Design for my dog training business Rustpaw Obedience

Need a business card design for my dog training business with my new logo. Want the card to come off professional yet fun. Want it to be very eye catchy as well. I normally have these at vet clinics, pet stores, and groomers. so need it to look better than my competitors.
Target Market(s)
dog owners
Industry/Entity Type
Dog Training
Contact Information for Business Card
needs logo, my name and info
Font styles to use
Serif
Colors
0255a3
ffffff
ec1f27
000000
333333
fbfbfb
Requirements
Must have
- Rustpaw Obedience
- Hollis Brandt
- 415 903 2267
- info@rustpawobedience.example
- www.rustpawobedience.example

```html
<!DOCTYPE html>
<html lang="en">
<head>
<meta charset="utf-8">
<title>Rustpaw Obedience — Business Card</title>
<link href="https://fonts.googleapis.com/css2?family=Lato:wght@400;700&family=Lora:ital,wght@0,700;1,400&display=swap" rel="stylesheet">
<style>
  :root {
    --red: #ec1f27;
    --black: #000000;
    --ink: #333333;
    --white: #ffffff;
    --paper: #fbfbfb;
    --stage: #e4e4e4;
  }
  html, body {
    margin: 0;
    padding: 0;
    width: 1200px;
    height: 900px;
    overflow: hidden;
    background: var(--stage);
  }
  .card {
    position: absolute;
    left: 100px;
    top: 160px;
    width: 1000px;
    height: 580px;
    background: linear-gradient(135deg, #e9e9e9 0%, var(--white) 40%, var(--paper) 100%);
    box-shadow: 0 14px 40px rgba(0,0,0,0.25);
    overflow: hidden;
    font-family: "Lato", sans-serif;
    color: var(--ink);
  }
  .brand {
    position: absolute;
    left: 70px;
    top: 70px;
  }
  .brand-name {
    font-family: "Lora", serif;
    font-weight: 700;
    font-size: 40px;
    color: var(--black);
    margin: 0;
    display: flex;
    align-items: center;
    gap: 14px;
  }
  .brand-mark {
    width: 22px;
    height: 22px;
    background: var(--black);
  }
  .tagline {
    font-family: "Lora", serif;
    font-style: italic;
    font-size: 15px;
    color: var(--black);
    margin: 12px 0 0 36px;
  }
  .divider {
    position: absolute;
    left: 70px;
    right: 70px;
    top: 262px;
    height: 2px;
    background: var(--red);
  }
  .contacts {
    position: absolute;
    left: 70px;
    top: 300px;
    list-style: none;
    margin: 0;
    padding: 0;
    font-size: 26px;
    line-height: 40px;
    color: var(--ink);
  }
  .contacts li {
    display: flex;
    align-items: center;
    gap: 14px;
  }
  .contacts svg {
    width: 16px;
    height: 16px;
    flex: none;
  }
  .person {
    position: absolute;
    right: 70px;
    top: 172px;
    text-align: right;
  }
  .person-name {
    font-family: "Lora", serif;
    font-weight: 700;
    font-size: 32px;
    letter-spacing: 1px;
    text-transform: uppercase;
    color: var(--red);
    margin: 0;
  }
  .person-role {
    font-size: 26px;
    color: var(--ink);
    margin: 4px 0 0;
  }
  .address {
    position: absolute;
    right: 70px;
    top: 300px;
    text-align: right;
    font-size: 28px;
    line-height: 38px;
    color: var(--ink);
    font-style: normal;
  }
  .footer-band {
    position: absolute;
    left: 0;
    bottom: 0;
    width: 1000px;
    height: 60px;
  }
</style>
</head>
<body>
  <main class="card">
    <header class="brand">
      <h1 class="brand-name"><span class="brand-mark"></span>Rustpaw Obedience</h1>
      <p class="tagline">“Calm dogs, happy homes, one lesson at a time.”</p>
    </header>

    <div class="person">
      <h2 class="person-name">Hollis Brandt</h2>
      <p class="person-role">Managing Director</p>
    </div>

    <div class="divider"></div>

    <ul class="contacts">
      <li>
        <svg viewBox="0 0 16 16" aria-hidden="true"><path d="M4 1 L6.5 4 L5 6 C6 8.5 7.5 10 10 11 L12 9.5 L15 12 L13 15 C7 15 1 9 1 3 Z" fill="var(--red)"/></svg>
        415 903 2267
      </li>
      <li>
        <svg viewBox="0 0 16 16" aria-hidden="true"><rect x="1" y="3" width="14" height="10" fill="none" stroke="var(--red)" stroke-width="1.6"/><path d="M1 3 L8 9 L15 3" fill="none" stroke="var(--red)" stroke-width="1.6"/></svg>
        info@rustpawobedience.example
      </li>
      <li>
        <svg viewBox="0 0 16 16" aria-hidden="true"><circle cx="8" cy="8" r="6.5" fill="none" stroke="var(--red)" stroke-width="1.5"/><ellipse cx="8" cy="8" rx="3" ry="6.5" fill="none" stroke="var(--red)" stroke-width="1.2"/><path d="M1.5 8 H14.5" stroke="var(--red)" stroke-width="1.2"/></svg>
        www.rustpawobedience.example
      </li>
    </ul>

    <address class="address">
      82b Harlow Lane,<br>
      Ashford, NZ, 7020
    </address>

    <svg class="footer-band" viewBox="0 0 1000 60" preserveAspectRatio="none" aria-hidden="true">
      <polygon points="0,0 370,0 330,60 0,60" fill="var(--black)"/>
      <polygon points="370,30 470,0 1000,0 1000,60 330,60" fill="var(--red)"/>
    </svg>
  </main>
</body>
</html>
```